Brennick Holdings Business Cards

These are professional business cards that are for my family office.
Put fake emails and phone numbers as of now until I finalize those components. This family office controls my families investments, assets, and future. The cards should be professional.
..
.
.
.
I just uploaded another variation of a logo I would like to see as a business card to I am inbeteen which logo to use

Target Market(s)

business

Industry/Entity Type

business

Contact Information for Business Card

Professional, wealth related, finance related.

Requirements
Must have
• Logo

```html
<!DOCTYPE html>
<html lang="en">
<head>
<meta charset="utf-8">
<title>Brennick Holdings Business Cards</title>
<link rel="stylesheet" href="https://fonts.googleapis.com/css2?family=Playfair+Display:wght@400;700&family=Arimo:wght@400&display=swap">
<style>
  :root {
    --backdrop: #161616;
    --card: #2a2a2c;
    --gold: #c3a66a;
    --white: #ffffff;
    --text: #f2f2f2;
  }
  * { margin: 0; padding: 0; box-sizing: border-box; }
  html, body {
    width: 1200px; height: 900px; overflow: hidden;
    background: var(--backdrop);
  }
  .canvas {
    position: relative; width: 1200px; height: 900px;
  }
  .card {
    position: absolute; left: 250px; width: 700px; height: 400px;
    background: var(--card); border-radius: 22px; overflow: hidden;
    box-shadow: 0 14px 30px rgba(0,0,0,0.55);
  }
  .card--front { top: 36px; }
  .card--back { top: 464px; }

  .wordmark {
    font-family: "Playfair Display", serif; font-weight: 400;
    color: var(--white); letter-spacing: 0.08em; text-transform: uppercase;
    display: flex; align-items: center; gap: 14px; white-space: nowrap;
  }
  .wordmark__square {
    width: 14px; height: 14px; background: var(--gold); flex: none;
  }
  .card--front .wordmark {
    position: absolute; left: 0; right: 0; top: 170px;
    justify-content: center; font-size: 46px;
  }
  .card--back .wordmark {
    position: absolute; right: 40px; top: 58px; font-size: 30px;
  }

  .holder {
    position: absolute; left: 40px; top: 190px;
  }
  .holder__name {
    font-family: "Playfair Display", serif; font-weight: 700;
    color: var(--gold); font-size: 27px; letter-spacing: 0.06em;
    text-transform: uppercase; line-height: 1.1;
  }
  .holder__title {
    font-family: "Arimo", sans-serif; color: var(--text);
    font-size: 18px; margin-top: 2px;
  }
  .divider {
    position: absolute; left: 40px; right: 40px; top: 262px;
    height: 1.5px; background: var(--gold);
  }
  .contacts {
    position: absolute; left: 40px; top: 276px; list-style: none;
    font-family: "Arimo", sans-serif; color: var(--text); font-size: 17px;
  }
  .contacts li {
    display: flex; align-items: center; gap: 10px; height: 26px;
  }
  .contacts svg { width: 15px; height: 15px; flex: none; }
  .address {
    position: absolute; right: 40px; top: 278px; text-align: right;
    font-family: "Arimo", sans-serif; color: var(--text);
    font-size: 17px; line-height: 1.4;
  }
  .edge-band {
    position: absolute; left: 0; bottom: 0; width: 700px; height: 22px;
  }
</style>
</head>
<body>
<main class="canvas">
  <section class="card card--front" aria-label="Card front">
    <div class="wordmark"><span class="wordmark__square"></span>Brennick Holdings</div>
  </section>

  <section class="card card--back" aria-label="Card back">
    <div class="wordmark"><span class="wordmark__square"></span>Brennick Holdings</div>

    <div class="holder">
      <p class="holder__name">Daniel Whitmore</p>
      <p class="holder__title">CEO/Founder</p>
    </div>

    <div class="divider"></div>

    <ul class="contacts">
      <li>
        <svg viewBox="0 0 16 16" aria-hidden="true"><path fill="#c3a66a" d="M3.2 1.5 5.6 1l1.3 3.2-1.6 1.1a9 9 0 0 0 5.4 5.4l1.1-1.6 3.2 1.3-.5 2.4c-.2.7-.8 1.2-1.5 1.2C6.6 14 2 9.4 2 3c0-.7.5-1.3 1.2-1.5z"/></svg>
        (555) 318-4470
      </li>
      <li>
        <svg viewBox="0 0 16 16" aria-hidden="true"><rect x="1" y="3" width="14" height="10" rx="1.5" fill="#c3a66a"/><path d="M1.8 4 8 9l6.2-5" fill="none" stroke="#2a2a2c" stroke-width="1.3"/></svg>
        DanielW@brennickholdings.com
      </li>
      <li>
        <svg viewBox="0 0 16 16" aria-hidden="true"><circle cx="8" cy="8" r="6.8" fill="none" stroke="#c3a66a" stroke-width="1.4"/><ellipse cx="8" cy="8" rx="2.8" ry="6.8" fill="none" stroke="#c3a66a" stroke-width="1.2"/><path d="M1.2 8h13.6" stroke="#c3a66a" stroke-width="1.2"/></svg>
        www.brennickholdings.com
      </li>
    </ul>

    <p class="address">4580 Larkspur Ave Suite 210<br>Fairhaven, AB 604218</p>

    <svg class="edge-band" viewBox="0 0 700 22" preserveAspectRatio="none" aria-hidden="true">
      <polygon points="0,0 440,0 425,22 0,22" fill="#ffffff"/>
      <polygon points="450,0 700,0 700,22 435,22" fill="#c3a66a"/>
    </svg>
  </section>
</main>
</body>
</html>
```